BRAVO San Felipe - For all your home service needs.

I need a web site designed for my new business called BRAVO San Felipe. This business is for the repair and servicing of home appliances and air conditioning systems and for plumbing and electrical repairs at residences. We will offer 1 year service contracts that provide for unlimited service calls and repairs of the equipment that is enrolled in the program. The business is located in San Felipe, Baja CA, Mexico which has a large population of retired American and Canadians. These are our target audience, not the Mexican population.

The business is an outgrowth of another business we own in San Felipe called Cardon Property Services which has been in business for 7 years and is well known and highly regarded in the community. The company is owned and operated by two Mexican nationals and an American who are all full time residents of San Felipe.

Our business model is the same as an American company called Bravo whose web site is https://www.keelhomecare.net/.

I already have a domain on HostPerch called www.bravohomefix.com and need a web design to populate this domain. We also have a Logo designed which I will upload for you.

Target Market(s)

The target audience is American and Canadian retirees who own homes and live in San Felipe either part time or full time.

Industry/Entity Type

Air Conditioning

Requirements
Must have
• The web site must have a home page, about us, service contracts, repairs, AC sales, Renewals, Quotes and Contact us pages. The information will be very similar to that shown for https://www.keelhomecare.net/.
Nice to have
• San Felipe is a desert community with an ocean (the gulf of California) so the design should incorporate some desert motifs and some seaside motifs. Also, should have some thoughts about how are services will make living in San Felipe worry free and enable the clients to enjoy life. One number to call for all their home service needs.
Should not have
• Do not have anything that belittles Mexico or Mexicans.

```html
<!DOCTYPE html>
<html lang="en">
<head>
<meta charset="utf-8">
<title>Bravo San Felipe</title>
<link href="https://fonts.googleapis.com/css2?family=Roboto:ital,wght@0,400;0,500;1,400&display=swap" rel="stylesheet">
<style>
:root{
  --red:#c8202b;
  --red-dark:#a3121c;
  --gold:#f6c84a;
  --amber:#f1a800;
  --charcoal:#3e3e3e;
  --text:#333;
  --sand:#f2d7a2;
  --card:#f3f3f3;
  --white:#fff;
}
*{box-sizing:border-box;margin:0;padding:0}
html,body{width:960px;height:1200px;overflow:hidden}
body{position:relative;font-family:'Roboto',sans-serif;color:var(--text);
  background:linear-gradient(180deg,#b7cfdc 0,#cfdbe0 80px,#6aa3b5 100px,#8fb6b5 300px,#e8cf9c 470px,var(--sand) 560px,var(--sand) 100%);}
.abs{position:absolute}
.brand{left:104px;top:22px;display:flex;align-items:center;gap:10px}
.brand-mark{width:44px;height:44px;border-radius:50%;background:var(--red)}
.brand-name{font-size:34px;font-weight:500;color:var(--red)}
.callbox{left:605px;top:16px;width:259px;height:68px;background:rgba(255,255,255,.85);border-radius:10px;padding:14px 0 0 12px}
.callbox svg{position:absolute;left:12px;top:16px}
.call-label{margin-left:30px;font-size:15px;color:var(--red);font-weight:500}
.call-nums{margin-left:30px;font-size:16px;color:#222;margin-top:2px;letter-spacing:.3px}
.nav{left:96px;top:100px;width:768px;height:38px;background:linear-gradient(#d02a33,var(--red-dark));border-radius:8px 8px 0 0;display:flex}
.nav a{color:var(--white);text-decoration:none;font-size:12.5px;letter-spacing:.5px;line-height:38px;text-align:center;border-right:1px solid #9a1018}
.nav a:last-child{border-right:none}
.page{left:96px;top:137px;width:768px;height:958px;background:var(--white);border-radius:0 0 10px 10px}
.hero{left:104px;top:141px;width:752px;height:327px;border-radius:8px;border:1px solid #ddd;background:linear-gradient(100deg,#ececec,#d6d6d6 40%,#f4f4f4 70%,#e4e4e4)}
.dots{left:439px;top:436px;display:flex;gap:6px}
.dots span{width:16px;height:16px;border-radius:50%;background:#555}
.dots span:first-child{background:#222}
h2{font-weight:400;font-size:19px;color:#333;letter-spacing:.3px}
.welcome{left:112px;top:482px;width:460px}
.welcome p{font-size:9.6px;line-height:17.6px;margin-top:6px;color:#333}
.rule{left:112px;top:723px;width:460px;height:1px;background:#ddd}
.wwd{left:112px;top:735px}
.card{top:771px;width:232px;height:308px;background:var(--card);border-radius:8px;overflow:hidden}
.card .ph{position:absolute;left:8px;top:9px;width:216px;height:110px;border-radius:6px}
.card h3{position:absolute;left:8px;top:135px;font-weight:500;font-size:15px;color:var(--red)}
.card ul{position:absolute;left:8px;top:160px;list-style:none}
.card li{font-size:10.5px;height:21.6px;padding-left:19px;position:relative;color:#333}
.card li svg{position:absolute;left:0;top:1px}
.more{position:absolute;left:0;bottom:0;height:33px;width:104px;background:var(--charcoal);color:var(--white);font-size:11.5px;line-height:33px;padding-left:14px;clip-path:polygon(0 0,86% 0,100% 100%,0 100%)}
.quote{left:616px;top:485px;width:233px;height:315px;background:var(--charcoal);border-radius:10px;padding:12px 17px}
.quote h2{color:var(--white);font-size:19px;margin-bottom:10px}
.field{height:23px;background:var(--white);border-radius:3px;margin-bottom:6.5px;font-size:10px;font-style:italic;color:#888;padding:5px 9px;position:relative}
.field.area{height:72px}
.field svg{position:absolute;right:8px;top:9px}
.submit{position:absolute;right:22px;top:275px;width:76px;height:26px;background:var(--amber);color:var(--white);font-size:12px;font-weight:500;text-align:center;line-height:26px;border-radius:3px}
.promo{left:616px;width:233px;height:86px;background:linear-gradient(#d5262f,var(--red-dark));border-radius:8px;border:2px solid #eee;text-align:center;color:var(--white);padding-top:9px}
.promo h4{font-weight:500;font-size:16.5px;letter-spacing:.5px}
.promo p{font-size:10.8px;color:var(--gold);line-height:13.6px;margin-top:3px}
.flinks{left:104px;top:1115px;font-size:10.8px;color:var(--red)}
.copy{left:104px;top:1149px;font-size:9.6px;color:#333}
.connect{left:735px;top:1111px;font-size:12px;color:#333}
.social{left:735px;top:1136px;display:flex;gap:8px}
.social span{width:24px;height:24px;border-radius:3px}
</style>
</head>
<body>
<div class="abs brand"><span class="brand-mark"></span><span class="brand-name">Bravo</span></div>
<div class="abs callbox">
  <svg width="18" height="18" viewBox="0 0 18 18"><rect width="18" height="18" rx="3" fill="#222"/><path d="M5 4c1-1 2 0 2.5 1.5s-.5 2-.5 2.5 1.5 3 3 3.5c.5 0 1-1 2.5-.5S14 13 13 14c-3 1-9-5-8-10z" fill="#fff"/></svg>
  <div class="call-label">Call Us Today:</div>
  <div class="call-nums">555 014 2290, 555 014 2291</div>
</div>
<nav class="abs nav">
  <a style="width:72px">Home</a><a style="width:97px">About us</a><a style="width:140px">Service Contracts</a><a style="width:85px">Repairs</a><a style="width:92px">AC Sales</a><a style="width:97px">Renewals</a><a style="width:86px">Quotes</a><a style="width:99px">Contact us</a>
</nav>
<div class="abs page"></div>
<div class="abs hero" role="img" aria-label="Technician cleaning a wall-mounted air conditioning unit"></div>
<div class="abs dots"><span></span><span></span><span></span><span></span></div>

<section class="abs welcome">
  <h2>Welcome to Bravo San Felipe</h2>
  <p>Aliquam molestie, mi et imperdiet euismod, dui purus auctor tellus, et interdum lacus lectus et ante. Sed accumsan sollicitudin sapien, sit amet adipiscing turpis gravida ac. In congue, neque ac lobortis volutpat, libero mauris varius mi, vitae suscipit ipsum ligula vitae risus. Duis aliquam nibh a dui iaculis viverra id a velit. Vivamus egestas risus in magna varius commodo. Sed semper viverra egestas. Etiam pretium porttitor lectus, vel ornare neque porta volutpat.</p>
  <p>Aliquam molestie, mi et imperdiet euismod, dui purus auctor tellus, et interdum lacus lectus et ante. Sed accumsan sollicitudin sapien, sit amet adipiscing turpis gravida ac. In congue, neque ac lobortis volutpat, libero mauris varius mi, vitae suscipit ipsum ligula vitae risus. Duis aliquam nibh a dui iaculis viverra id a velit. Vivamus egestas risus in magna varius commodo. Sed semper viverra egestas. Etiam pretium porttitor lectus, vel ornare neque porta volutpat.</p>
</section>
<div class="abs rule"></div>
<h2 class="abs wwd">What We Do</h2>

<svg width="0" height="0" style="position:absolute"><defs><symbol id="tick" viewBox="0 0 12 12"><path d="M1 6.5l3 3L11 1.5" stroke="#c8202b" stroke-width="2.2" fill="none"/></symbol></defs></svg>

<div class="abs card" style="left:112px">
  <div class="ph" role="img" aria-label="Two-storey family house with lawn and trees" style="background:linear-gradient(#8fb0d8,#b9a98c 55%,#5f7d3a)"></div>
  <h3>Residential Services</h3>
  <ul>
    <li><svg width="10" height="10"><use href="#tick"/></svg>Residential Service Contracts</li>
    <li><svg width="10" height="10"><use href="#tick"/></svg>Residential Air Conditioning Sales</li>
    <li><svg width="10" height="10"><use href="#tick"/></svg>Residential Repairs</li>
    <li><svg width="10" height="10"><use href="#tick"/></svg>Residential Plumbing Services</li>
    <li><svg width="10" height="10"><use href="#tick"/></svg>Residential Electrical Repair</li>
  </ul>
  <div class="more">READ MORE</div>
</div>
<div class="abs card" style="left:368px">
  <div class="ph" role="img" aria-label="Modern glass office building" style="background:linear-gradient(#3b6fc4,#9fb7d8 55%,#8a8a8a)"></div>
  <h3>Commercial Services</h3>
  <ul>
    <li><svg width="10" height="10"><use href="#tick"/></svg>Community Service Contracts</li>
    <li><svg width="10" height="10"><use href="#tick"/></svg>Commercial Air Conditioning Sales</li>
    <li><svg width="10" height="10"><use href="#tick"/></svg>Commercial Repairs</li>
    <li><svg width="10" height="10"><use href="#tick"/></svg>Commercial Plumbing Services</li>
    <li><svg width="10" height="10"><use href="#tick"/></svg>Commercial Electrical Repair</li>
  </ul>
  <div class="more">READ MORE</div>
</div>

<form class="abs quote">
  <h2>Get a FREE Quotes</h2>
  <div class="field">Name</div>
  <div class="field">Email Address</div>
  <div class="field">Contact Number</div>
  <div class="field">Property Zip Code</div>
  <div class="field">Do You Have an Active Contract<svg width="12" height="6"><path d="M0 0h12L6 6z" fill="#444"/></svg></div>
  <div class="field area">How Can We Help You?</div>
  <div class="submit">SUBMIT</div>
</form>

<div class="abs promo" style="top:808px"><h4>SERVICE CONTRACT</h4><p>Costs Just $26 Per Month, No<br>Deductibles, Completely Customizable,<br>24 Hour Emergency Service</p></div>
<div class="abs promo" style="top:901px"><h4>AIR CONDITIONING SALES</h4><p>Top Brands, Lowest Prices<br>Free Quotes,<br>Will Beat Any Competitor Offer</p></div>
<div class="abs promo" style="top:994px"><h4>REPAIRS RIGHT NOW</h4><p>Residential and Commercial<br>Appliances, AC, Plumbing, Electrical,<br>24 Hour Emergency Service</p></div>

<div class="abs flinks">Home &nbsp;/&nbsp; About us &nbsp;/&nbsp; Service Contracts &nbsp;/&nbsp; Repairs AC Sales / Renewals / Quotes &nbsp;/ Contact us</div>
<div class="abs copy">Copyright © 2012. Bravo San Felipe. All Right Reserved</div>
<div class="abs connect">Connect Us</div>
<div class="abs social"><span style="background:#3b5b98"></span><span style="background:#4fb6e3"></span><span style="background:#f08a1c"></span><span style="background:#c8202b"></span></div>
</body>
</html>
```